Rashwan hotel

Kindly design a profile for our hotel, you an find attached the original profile witch needs a lot of work and alteration, kindly upgrade the design to be more professional. And you can find attached the logo (you are welcome to play with it).

```html
<!DOCTYPE html>
<html lang="en">
<head>
<meta charset="utf-8">
<title>Rashwan Hotel – Profile Pages</title>
<link rel="stylesheet" href="https://fonts.googleapis.com/css2?family=Jost:wght@300;400;500;600;700&display=swap">
<style>
  :root{
    --board:#5e5e5e;
    --paper:#f7f7f7;
    --yellow:#ffdd00;
    --ink:#151515;
    --grey-band:#e2e2e2;
    --label:#ffffff;
    --font:'Jost', sans-serif;
  }
  *{box-sizing:border-box;margin:0;padding:0}
  html,body{width:962px;height:1200px;overflow:hidden;background:var(--board)}
  body{font-family:var(--font);color:var(--ink);position:relative}
  .page{position:absolute;width:436px;height:326px;background:var(--paper);overflow:hidden;
        box-shadow:0 14px 18px -8px rgba(0,0,0,.45)}
  .page svg.layer{position:absolute;left:0;top:0;width:436px;height:326px}
  .label{position:absolute;width:436px;text-align:center;color:var(--label);font-size:16px;font-weight:400;letter-spacing:.5px}

  /* cover */
  .cover-brand{position:absolute;right:19px;top:70px;text-align:left}
  .cover-brand .name{font-size:12.5px;font-weight:500;letter-spacing:.2px}
  .cover-brand .tag{font-size:5px;letter-spacing:1.2px;margin-top:2px}
  .cover-title{position:absolute;left:9px;top:152px;line-height:1}
  .cover-title .t1{font-size:28px;font-weight:300;letter-spacing:.5px}
  .cover-title .t2{font-size:26px;font-weight:700;margin-top:4px;letter-spacing:.5px}
  .cover-title .t3{font-size:42px;font-weight:700;margin-top:1px;letter-spacing:.5px}
  .cover-rule{position:absolute;left:9px;top:262px;width:57px;height:2px;background:var(--ink)}
  .cover-blurb{position:absolute;left:9px;top:273px;font-size:6.2px;line-height:1.5}
  .cover-web{position:absolute;left:0;top:304px;width:118px;height:15px;background:var(--ink);color:#fff;
             border-radius:0 8px 8px 0;font-size:6px;letter-spacing:.8px;padding-left:10px;line-height:15px}
  .cover-web::before{content:"";display:inline-block;width:5px;height:5px;border:1px solid #fff;border-radius:50%;margin-right:4px;vertical-align:-1px}

  /* index */
  .index{background:var(--yellow)}
  .index-title{position:absolute;left:87px;top:12px;font-size:21px;font-weight:400;letter-spacing:.3px}
  .index-rule{position:absolute;left:138px;top:42px;right:0;height:1.5px;background:var(--ink)}
  .index-list{position:absolute;left:38px;top:65px;list-style:none}
  .index-list li{position:relative;height:18.2px;font-size:7.2px;width:196px}
  .index-list li::after{content:"- - - - - - - - - - - - - - - - -";position:absolute;left:80px;top:0;font-size:6.5px;letter-spacing:.2px}
  .index-list .num{position:absolute;left:180px}

  /* inner pages */
  .head-title{position:absolute;left:7px;top:8px;font-size:17.5px;font-weight:400;letter-spacing:.2px}
  .head-rule{position:absolute;left:7px;top:31px;width:412px;height:1.2px;background:var(--ink)}
  .head-brand{position:absolute;right:8px;top:37px;text-align:right}
  .head-brand .name{font-size:6.5px;font-weight:600}
  .head-brand .tag{font-size:2.6px;letter-spacing:.4px}
  .foot{position:absolute;left:10px;top:310px;font-size:5px;padding-bottom:2px;border-bottom:1.5px solid var(--yellow);width:218px}
  .folio{position:absolute;right:11px;top:310px;font-size:5px;padding-bottom:2px;border-bottom:1.5px solid var(--yellow);width:10px;text-align:center}
  .photo{position:absolute}

  /* sign-off */
  .signoff{position:absolute;left:494px;top:990px;width:436px;text-align:center;color:#fff}
  .signoff .name{font-size:29px;font-weight:500;letter-spacing:.5px}
  .signoff .tag{font-size:11.5px;letter-spacing:2.6px;margin-top:6px;color:#e8e8e8}
</style>
</head>
<body>

<!-- Cover -->
<section class="page cover" style="left:30px;top:28px">
  <svg class="layer" viewBox="0 0 436 326">
    <defs>
      <linearGradient id="interior" x1="0" y1="0" x2="1" y2="1">
        <stop offset="0" stop-color="#d9d4cc"/>
        <stop offset=".55" stop-color="#b9ab98"/>
        <stop offset="1" stop-color="#7a2a2a"/>
      </linearGradient>
    </defs>
    <polygon points="0,104 118,104 236,0 264,0 130,124 0,124" fill="var(--grey-band)"/>
    <polygon points="0,124 130,124 436,124 436,326 0,326" fill="var(--yellow)"/>
    <polygon points="118,124 230,12 300,80 344,108 436,150 436,326 306,326" fill="url(#interior)" role="img" aria-label="Hotel interior with lanterns and patterned screens"/>
    <g stroke="#fff" stroke-width="2.5" fill="none">
      <line x1="300" y1="80" x2="160" y2="220"/>
      <line x1="344" y1="108" x2="200" y2="252"/>
      <line x1="230" y1="12" x2="436" y2="218"/>
      <line x1="436" y1="190" x2="306" y2="326"/>
      <line x1="180" y1="124" x2="380" y2="326"/>
    </g>
    <polygon points="238,8 258,28 238,48 218,28" fill="var(--ink)"/>
  </svg>
  <div class="cover-brand"><div class="name">RASHWAN HOTEL</div><div class="tag">YOUR HOME AWAY FROM HOME</div></div>
  <div class="cover-title">
    <div class="t1">RASHWAN</div>
    <div class="t2">BOUTIQUE</div>
    <div class="t3">HOTEL</div>
  </div>
  <div class="cover-rule"></div>
  <p class="cover-blurb">Lorem Ipsum is simply dummy text of the printing and typesetting industry.<br>Lorem Ipsum has been the industry's standard dummy text ever.</p>
  <div class="cover-web">www.rashwanstay.net</div>
</section>
<div class="label" style="left:30px;top:376px">COVER PAGE</div>

<!-- Index -->
<section class="page index" style="left:494px;top:28px">
  <h1 class="index-title">THE INDEX</h1>
  <div class="index-rule"></div>
  <ol class="index-list">
    <li>Reception Hall<span class="num">02</span></li>
    <li>Reception Lounge<span class="num">03</span></li>
    <li>Entrance Hall<span class="num">04</span></li>
    <li>Reception Desk<span class="num">05</span></li>
    <li>Reception Hall<span class="num">06</span></li>
    <li>Floor Layout<span class="num">10</span></li>
    <li>Elevator Hall<span class="num">11</span></li>
    <li>Corridor<span class="num">12</span></li>
    <li>Façade concept<span class="num">14</span></li>
    <li>Store windows<span class="num">15</span></li>
    <li>Front Elevations<span class="num">17</span></li>
    <li>Side Elevations<span class="num">18</span></li>
    <li>Parking option 1<span class="num">19</span></li>
    <li>Parking option 2<span class="num">20</span></li>
  </ol>
  <svg class="layer" viewBox="0 0 436 326">
    <defs>
      <linearGradient id="pool" x1="0" y1="1" x2="1" y2="0">
        <stop offset="0" stop-color="#2e5f86"/>
        <stop offset=".6" stop-color="#5c87a6"/>
        <stop offset="1" stop-color="#c9c2b4"/>
      </linearGradient>
    </defs>
    <polygon points="254,326 436,144 436,326" fill="url(#pool)" role="img" aria-label="Hotel pool with tiled floor and lit columns"/>
    <g stroke="#fff" stroke-width="2" fill="none">
      <line x1="300" y1="326" x2="400" y2="226"/>
      <line x1="380" y1="200" x2="436" y2="256"/>
      <line x1="330" y1="250" x2="406" y2="326"/>
    </g>
  </svg>
</section>
<div class="label" style="left:494px;top:376px">PAGE - 01</div>

<!-- Reception Hall -->
<section class="page" style="left:30px;top:419px">
  <h2 class="head-title">RECEPTION HALL</h2>
  <div class="head-rule"></div>
  <div class="head-brand"><div class="name">RASHWAN HOTEL</div><div class="tag">YOUR HOME AWAY FROM HOME</div></div>
  <div class="photo" role="img" aria-label="Reception hall with tall wooden columns and lounge chairs"
       style="left:12px;top:68px;width:414px;height:222px;background:linear-gradient(180deg,#b9b3ad 0%,#7d6c62 45%,#4a3b35 70%,#8d8784 100%)"></div>
  <svg class="layer" viewBox="0 0 436 326">
    <polygon points="12,68 80,68 12,125" fill="var(--yellow)"/>
    <polygon points="426,233 426,291 356,291" fill="var(--yellow)"/>
  </svg>
  <div class="foot">Copyright © 2018 RASHWAN BOUTIQUE HOTEL &nbsp;|&nbsp; www.rashwanstay.net</div>
  <div class="folio">02</div>
</section>
<div class="label" style="left:30px;top:768px">PAGE - 02</div>

<!-- Reception Lounge -->
<section class="page" style="left:494px;top:419px">
  <h2 class="head-title">RECEPTION LOUNGE</h2>
  <div class="head-rule"></div>
  <div class="head-brand"><div class="name">RASHWAN HOTEL</div><div class="tag">YOUR HOME AWAY FROM HOME</div></div>
  <div class="photo" role="img" aria-label="Lounge entrance framed by carved wooden screens"
       style="left:13px;top:68px;width:193px;height:222px;background:linear-gradient(90deg,#5a3a24 0%,#c9c2b6 35%,#d8dde0 50%,#c9c2b6 65%,#5a3a24 100%)"></div>
  <div class="photo" role="img" aria-label="Lounge seating under hanging lights and wooden slats"
       style="left:230px;top:68px;width:192px;height:222px;background:linear-gradient(180deg,#6b5138 0%,#9b7a57 40%,#3d3b39 70%,#c8c1b6 100%)"></div>
  <svg class="layer" viewBox="0 0 436 326" fill="none" stroke="#fff" stroke-width="1">
    <polyline points="20,100 20,74 60,74"/>
    <polyline points="198,260 198,284 160,284"/>
    <polyline points="236,108 236,74 276,74"/>
    <polyline points="416,250 416,284 380,284"/>
  </svg>
  <div class="foot">Copyright © 2018 RASHWAN BOUTIQUE HOTEL &nbsp;|&nbsp; www.rashwanstay.net</div>
  <div class="folio">03</div>
</section>
<div class="label" style="left:494px;top:768px">PAGE - 03</div>

<!-- Entrance Hall -->
<section class="page" style="left:30px;top:810px">
  <h2 class="head-title">ENTRANCE HALL</h2>
  <div class="head-rule"></div>
  <div class="head-brand"><div class="name">RASHWAN HOTEL</div><div class="tag">YOUR HOME AWAY FROM HOME</div></div>
  <svg class="layer" viewBox="0 0 436 326" stroke="var(--yellow)" stroke-width="1.5">
    <line x1="54" y1="98" x2="388" y2="98"/>
    <line x1="142" y1="104" x2="418" y2="104"/>
    <line x1="54" y1="241" x2="330" y2="241"/>
    <line x1="86" y1="247" x2="416" y2="247"/>
  </svg>
  <div class="photo" role="img" aria-label="Front elevation drawing of the entrance hall with glazed doors"
       style="left:20px;top:119px;width:400px;height:107px;background:linear-gradient(180deg,#fafafa 0%,#8a6a55 15%,#5b4a3f 50%,#4d7c86 70%,#e9e6e2 100%);border:1px solid #bbb"></div>
  <div class="foot">Copyright © 2018 RASHWAN BOUTIQUE HOTEL &nbsp;|&nbsp; www.rashwanstay.net</div>
  <div class="folio">04</div>
</section>
<div class="label" style="left:30px;top:1152px">PAGE - 04</div>

<!-- Sign-off -->
<div class="signoff">
  <div class="name">RASHWAN HOTEL</div>
  <div class="tag">YOUR HOME AWAY FROM HOME</div>
</div>

</body>
</html>
```